Card design for orthopaedic surgeons working as The Meridale Orthopaedic Clinic

Business cards, letterhead

Colors

Designer to choose colors to be used in the design.

Requirements
Must have
• Late addition.
• Cards letterhead must have logos of
• Corvane Federated Guild of Surgeons
• Tellmark Orthopaedic Society
Nice to have
• Back of card to have space for appointment time to be added by hand and some blank space for writing incidental other notes.

```html
<!DOCTYPE html>
<html lang="en">
<head>
<meta charset="utf-8">
<title>The Meridale Orthopaedic Clinic — Letterhead</title>
<link href="https://fonts.googleapis.com/css2?family=Montserrat:wght@400&display=swap" rel="stylesheet">
<style>
  :root {
    --backdrop: #d8d8d8;
    --paper: #ffffff;
    --brand-blue: #14a9e3;
    --ink: #2b2b2b;
  }
  * { margin: 0; padding: 0; box-sizing: border-box; }
  html, body { width: 1200px; height: 1000px; overflow: hidden; }
  body {
    background: var(--backdrop);
    font-family: "Montserrat", Arial, sans-serif;
    color: var(--ink);
    position: relative;
  }
  .letterhead {
    position: absolute;
    left: 263px; top: 38px;
    width: 658px; height: 923px;
    background: var(--paper);
  }
  .brand-name {
    position: absolute;
    left: 40px; top: 58px;
    font-size: 21px;
    font-weight: 400;
    letter-spacing: -0.4px;
    color: var(--brand-blue);
    white-space: nowrap;
  }
  .contact-block {
    position: absolute;
    left: 39px; top: 865px;
    font-size: 9px;
    line-height: 13.5px;
  }
  .contact-row { display: flex; align-items: center; gap: 6px; white-space: nowrap; }
  .contact-item { display: inline-flex; align-items: center; gap: 4px; }
  .icon { width: 12px; height: 12px; flex: none; }
  .social-handle {
    position: absolute;
    right: 39px; top: 878px;
    display: flex; align-items: center; gap: 5px;
    font-size: 9.5px;
  }
  .social-dot {
    width: 13px; height: 13px; border-radius: 50%;
    background: var(--brand-blue);
  }
</style>
</head>
<body>
  <main class="letterhead">
    <header class="brand-name">The Meridale Orthopaedic Clinic</header>

    <footer>
      <div class="contact-block">
        <div class="contact-row">
          <span class="contact-item">
            <svg class="icon" viewBox="0 0 12 12" aria-hidden="true">
              <circle cx="6" cy="6" r="6" fill="var(--brand-blue)"/>
              <path d="M6 2.4a2.4 2.4 0 0 1 2.4 2.4C8.4 6.6 6 9.4 6 9.4S3.6 6.6 3.6 4.8A2.4 2.4 0 0 1 6 2.4z" fill="#fff"/>
              <circle cx="6" cy="4.8" r="0.9" fill="var(--brand-blue)"/>
            </svg>
            USA | Street 9 | Block 2 | Floor 4 | Room 16
          </span>
        </div>
        <div class="contact-row">
          <span class="contact-item">
            <svg class="icon" viewBox="0 0 12 12" aria-hidden="true">
              <circle cx="6" cy="6" r="6" fill="var(--brand-blue)"/>
              <path d="M3.7 3c.4-.3.8-.3 1 .1l.6 1.1c.2.3.1.6-.2.9l-.3.3c.3.7.9 1.3 1.6 1.6l.3-.3c.3-.3.6-.4.9-.2l1.1.6c.4.2.4.6.1 1-.6.7-1.4.9-2.4.4C5 8 4 7 3.5 5.6 3.1 4.5 3.2 3.6 3.7 3z" fill="#fff"/>
            </svg>
            313-MER-456
          </span>
          <span class="contact-item">
            <svg class="icon" viewBox="0 0 12 12" aria-hidden="true">
              <circle cx="6" cy="6" r="6" fill="var(--brand-blue)"/>
              <rect x="3" y="4" width="6" height="4.2" rx="0.5" fill="none" stroke="#fff" stroke-width="0.8"/>
              <path d="M3.2 4.3 6 6.4l2.8-2.1" fill="none" stroke="#fff" stroke-width="0.8"/>
            </svg>
            info@meridaleortho.com
          </span>
          <span class="contact-item">
            <svg class="icon" viewBox="0 0 12 12" aria-hidden="true">
              <circle cx="6" cy="6" r="5.4" fill="none" stroke="var(--brand-blue)" stroke-width="1.1"/>
              <ellipse cx="6" cy="6" rx="2.2" ry="5.4" fill="none" stroke="var(--brand-blue)" stroke-width="0.9"/>
              <path d="M0.8 6h10.4M1.6 3.4h8.8M1.6 8.6h8.8" stroke="var(--brand-blue)" stroke-width="0.8"/>
            </svg>
            www.meridaleortho.com
          </span>
        </div>
      </div>

      <div class="social-handle">
        <span class="social-dot" aria-hidden="true"></span>
        mrd_ortho
      </div>
    </footer>
  </main>
</body>
</html>
```